Resume: Professional Marketer seeking to impress potential recruiters with my skills & experience

Create a marketing esque style CV. I'm an outgoing, driven marketing with years of experience. I'm looking for a new senior role. My CV should look professional, but with elements of creativity and be a little bold. It should stand out amongst all the other CVs being submitted for a role. Check out my crewbase profile here: https://www.crewbase.example/in/marisol-tovrek-58210394/ I would like to include a photo with the design, as a subtle element of the design.

Target Market(s)

Recruiters, Headhunters

Industry/Entity Type

Marketing

Font styles to use
Sans Serif

Requirements
Must have
• Easy to read sections, with enough detail for a recruiter to understand my experience.
Nice to have
• Graphics, icons etc to represent experience

```html
<!DOCTYPE html>
<html lang="en">
<head>
<meta charset="utf-8">
<title>Marisol Tovrek – Resume</title>
<link href="https://fonts.googleapis.com/css2?family=Montserrat:wght@600;700;800&family=Open+Sans:wght@400;600;700&display=swap" rel="stylesheet">
<style>
:root{
  --blue:#1b9ae4;
  --sky:#c9edfb;
  --ink:#3a3a3a;
  --muted:#777;
  --label:#8a8a8a;
  --stage:#e4e4e4;
  --paper:#ffffff;
}
*{box-sizing:border-box;margin:0;padding:0}
html,body{width:1200px;height:1200px;overflow:hidden}
body{background:var(--stage);font-family:"Open Sans",Arial,sans-serif;color:var(--ink);position:relative}
.page{position:absolute;width:342px;height:484px;background:var(--paper);overflow:hidden;box-shadow:0 0 0 1px #d6d6d6}
.page-label{position:absolute;width:342px;text-align:center;font:700 22px/1 "Open Sans",Arial,sans-serif;color:var(--label);letter-spacing:.5px}
.band{position:absolute;left:0;width:100%;height:8px;background:linear-gradient(90deg,var(--blue) 0 42%,var(--sky) 42% 58%,var(--blue) 58% 100%)}
.band.top{top:0}.band.bottom{bottom:0}

/* page 1 */
.sidebar{position:absolute;left:0;top:0;width:122px;height:484px;background:var(--blue);color:#fff}
.sidebar svg.deco{position:absolute;left:0;top:0}
.photo{position:absolute;left:16px;top:16px;width:92px;height:92px;border-radius:50%;background:radial-gradient(circle at 50% 40%,#e9c9a8,#b38a62 70%,#8c6a48);border:3px solid #fff}
.name{position:absolute;left:16px;top:116px;font:700 10.5px/1 Montserrat,sans-serif;letter-spacing:.3px;white-space:nowrap}
.locale{position:absolute;left:16px;top:134px;padding-top:5px;border-top:1px solid rgba(255,255,255,.6);width:96px;font:600 4.9px/1 Montserrat,sans-serif;letter-spacing:.1px;white-space:nowrap}
.skills-title{position:absolute;left:16px;top:289px;font:700 6.4px/1 Montserrat,sans-serif;white-space:nowrap}
.skills{position:absolute;left:16px;top:300px;width:104px;border-top:1px solid rgba(255,255,255,.5);padding-top:4px;display:grid;grid-template-columns:repeat(3,1fr);row-gap:8px;column-gap:3px;font:600 3.4px/1.3 "Open Sans",sans-serif}
.main{position:absolute;left:136px;top:0;right:0;height:484px}
.sec-head{position:relative;display:flex;align-items:center;font:700 6.4px/1 Montserrat,sans-serif;color:#222;white-space:nowrap}
.sec-head .bar{flex:1;height:6px;margin-left:6px;background:linear-gradient(90deg,transparent 0 2px,var(--blue) 2px 5px,transparent 5px 7px,var(--blue) 7px 10px,transparent 10px 12px,var(--blue) 12px 15px,transparent 15px 17px,var(--blue) 17px);clip-path:polygon(3px 0,100% 0,100% 100%,0 100%)}
.intro{position:absolute;left:0;right:0;top:16px}
.txt{font-size:3.4px;line-height:1.45;color:var(--muted)}
.txt p{margin-top:4px;padding-right:16px}
.record{position:absolute;left:0;right:0;top:110px}
.rec-table{margin-top:7px;display:grid;grid-template-columns:43px 82px 1fr;row-gap:5px;font-size:3.3px;line-height:1.4;color:var(--muted);padding-right:12px}
.exp{position:absolute;left:0;right:0;top:376px}

/* role blocks */
.role{position:absolute;left:18px;right:18px}
.row{display:grid;grid-template-columns:66px 1fr;margin-bottom:7px;font-size:3.3px;line-height:1.5;color:var(--muted)}
.date{font:700 3.5px/1.4 "Open Sans",sans-serif;color:var(--blue)}
.col p{margin-bottom:3px}
.col ul{list-style:none;margin-bottom:3px}
.col li{position:relative;padding-left:5px;margin-bottom:2px}
.col li::before{content:"";position:absolute;left:0;top:1.6px;width:1.8px;height:1.8px;border-radius:50%;background:var(--blue)}
.stack span{display:block;margin-bottom:3px}
.exp .row{grid-template-columns:60px 1fr;padding-right:14px}

/* page 5 */
.contact-bar{position:absolute;left:0;right:0;top:194px;height:20px;background:var(--blue);color:#fff;font:700 4.6px/20px Montserrat,sans-serif;padding-left:16px;white-space:nowrap}
.contact-icon{position:absolute;left:164px;top:180px;width:16px;height:16px;border-radius:50%;background:var(--blue);border:1.5px solid #fff;display:flex;align-items:center;justify-content:center}
.p5-sec{position:absolute;left:16px;right:0}
.q-grid{display:grid;grid-template-columns:1fr 1fr;column-gap:10px;row-gap:14px;margin-top:14px;padding-right:16px}
.tl{position:relative;padding-left:14px;font-size:3.2px;line-height:1.4;color:var(--muted)}
.tl::before{content:"";position:absolute;left:2px;top:0;bottom:2px;width:.8px;background:var(--blue)}
.tl div{display:grid;grid-template-columns:26px 1fr;margin-bottom:8px;position:relative}
.tl div::before{content:"";position:absolute;left:-13.5px;top:1px;width:2.6px;height:2.6px;border-radius:50%;background:var(--blue)}
.ee-grid{display:grid;grid-template-columns:repeat(3,1fr);column-gap:6px;margin-top:12px;padding-right:16px}
.ee-grid .tl{padding-left:10px}
.ee-grid .tl div{grid-template-columns:20px 1fr}
.ee-grid .tl div::before{left:-9.5px}
.small-note{font-size:3.3px;color:var(--muted);margin-top:10px}
</style>
</head>
<body>

<!-- PAGE 1 -->
<section class="page" style="left:24px;top:36px">
  <aside class="sidebar">
    <svg class="deco" width="122" height="484" viewBox="0 0 122 484" aria-hidden="true">
      <polygon points="0,160 122,210 122,250 0,200" fill="#7fd0f4" opacity=".6"/>
      <polygon points="0,200 122,250 122,272 0,230" fill="#c9edfb" opacity=".8"/>
      <polygon points="0,230 80,262 0,270" fill="#ffffff" opacity=".9"/>
      <polygon points="0,430 122,470 122,484 0,484" fill="#ffffff"/>
      <polygon points="0,400 122,450 122,470 0,430" fill="#c9edfb" opacity=".7"/>
    </svg>
    <div class="photo" role="img" aria-label="Portrait photo of Marisol Tovrek"></div>
    <div class="name">MARISOL TOVREK</div>
    <div class="locale">HARBOUR VALE NSW 0400 555 218</div>
    <div class="skills-title">KEY SKILLS AND EXPERIENCE</div>
    <div class="skills">
      <span>Advertising</span><span>Digital Marketing</span><span>Media Planning</span>
      <span>Branding</span><span>Distribution</span><span>People Management</span>
      <span>Budgeting &amp; Forecasting</span><span>Direct Marketing</span><span>Product Development</span>
      <span>Business Analysis</span><span>Executive Reporting</span><span>P&amp;L Responsibility</span>
      <span>Call Centres</span><span>Financial Modelling</span><span>Retention</span>
      <span>Customer Acquisition</span><span>Lead Generation</span><span>Sales</span>
      <span>Customer Retention</span><span>Marketing Analysis</span><span>Strategy Development</span>
      <span>Copy Writing</span><span>Marketing</span><span>Stakeholder Management</span>
    </div>
  </aside>
  <div class="main">
    <div class="intro">
      <h2 class="sec-head">INTRODUCTION<span class="bar"></span></h2>
      <div class="txt">
        <p>I am a passionate direct marketer of 15+ years experience in Australia, plus key roles in startup organisations in London and New York.</p>
        <p>I am a talented consumer marketer with strong commercial and business acumen. I played a fundamental role in the growth of CoverPoint Pty Ltd, to become the number one direct life insurance brand in Australia.</p>
        <p>As a strategic marketer, my strengths lie in analytical thinking and the ability to translate marketing and sales activity into commercial modelling, and ultimately profitability.</p>
        <p>I am a talented professional with the drive to succeed. I have benefited from working alongside exceptional people, who have helped me develop personally, and as a leader. My goal now is to engage with as many strategic and intellectual minds as possible, and to help others develop to achieve theirs.</p>
      </div>
    </div>
    <div class="record">
      <h2 class="sec-head">EMPLOYMENT RECORD (LAST 15 YEARS)<span class="bar"></span></h2>
      <div class="rec-table">
        <span>May 2016<br>to Current</span><span>Marketing Strategy Consultant</span><span>Clients include Spokewise, Alpen Re, Tallow Studio, Supper Sorted</span>
        <span>January 2011<br>to Current</span><span>Marketer and Business Development</span><span>Mika Grant Studio</span>
        <span>August 2015<br>to May 2016</span><span>Career break</span><span></span>
        <span>April 2015<br>to August 2015</span><span>Head of Marketing</span><span>Northgate Life Distribution (US) Harbourline Life (life insurance brand)</span>
        <span>August 2014<br>to April 2015</span><span>Maternity Leave – to my son</span><span></span>
        <span>March 2014<br>to August 2014</span><span>General Manager Marketing and Business Operations</span><span>Northgate Life Distribution (UK) Prentis Life (life insurance brand)</span>
        <span>May 2013<br>to April 2014</span><span>Career break</span><span></span>
        <span>October 2013</span><span>Consultant – New Business Proposal</span><span>Overview Admin Services Pty Limited</span>
        <span>December 2012<br>to May 2013</span><span>Commercial &amp; MIS Manager</span><span>Keel Assurance Ltd</span>
        <span>July 2012<br>to December 2012</span><span>Head of Marketing Operations – Acquisition and Retention</span><span>Keel Assurance Ltd</span>
        <span>October 2010<br>to July 2012</span><span>P&amp;L / Brand Manager – CoverPoint</span><span>Keel Assurance Ltd</span>
        <span>January 2010<br>to October 2010</span><span>Product Portfolio Marketing Manager – CoverPoint</span><span>Keel Assurance Ltd (previously Spire)</span>
        <span>January 2008<br>to October 2010</span><span>Marketing Manager – CoverPoint</span><span>Keel Assurance Ltd (CoverPoint Pty Limited was acquired by Keel in September 2008)</span>
        <span>February 2007<br>to December 2007</span><span>Database and Retention Strategy Manager</span><span>CoverPoint Pty Limited, Harbour Vale office relocation</span>
        <span>July 2004<br>to January 2007</span><span>Direct Marketing Specialist</span><span>CoverPoint Pty Limited</span>
        <span>April 2002<br>to June 2004</span><span>Acquisition and Database Marketing Manager – Japan</span><span>Valuehouse Pty Ltd (currently known as Valuehouse Pty Ltd)</span>
      </div>
    </div>
    <div class="exp">
      <h2 class="sec-head">EXPERIENCE &amp; RESPONSBILITIES FOR EACH ROLE<span class="bar"></span></h2>
      <div class="row" style="margin-top:7px"><span class="date">MAY 2016 TO MAY 2018</span><span>Marketing Strategy Consultant</span></div>
      <div class="row"><span>Role responsibilities -</span><div class="col">
        <p>Working with businesses – large and small – to drive and execute change in order to achieve their corporate and financial goals.</p>
        <p>Consulting services include developing and implementing new and existing marketing strategy, product strategy, and customer experience. Building their business and financial positions through understanding the sales process and customer path to purchase, implementing process improvement, and through improved forecasting, and cost and budget management.</p>
        <p>Primary key stakeholders are the clients management team, their teams, agencies, and suppliers.</p>
      </div></div>
      <div class="row"><span>Reporting to -<br>Key Relationships -</span><span>Clients include Spokewise, Alpen Re, Tallow Studio, Supper Sorted, Haven Health.</span></div>
    </div>
  </div>
</section>
<div class="page-label" style="left:24px;top:542px">PAGE - 01</div>

<!-- PAGE 2 -->
<section class="page" style="left:426px;top:36px">
  <div class="band top"></div>
  <div class="role" style="top:30px">
    <div class="row"><span class="date">APRIL 2015 TO AUGUST 2015</span><span>Head of Marketing<br>Northgate Life Distribution (US) - Harbourline Life, consumer life insurance brand</span></div>
    <div class="row"><span>Role responsibilities -</span><div class="col">
      <p>The overarching objectives of the Head of Marketing role were to -</p>
      <ul><li>To prepare Harbourline Life for the launch of the Direct Life Insurance brand.</li><li>To achieve the operational new business plan (sales units, revenue &amp; acquisition expenditure), with the Head of Sales.</li><li>To recruit Chief Marketing Officer to replace me (upon the planned move to Northgate Life Distribution UK, as the role of Chief Marketing Officer, UK).</li></ul>
      <p>The objectives of the Head of Marketing -</p>
      <ul><li>To develop and execute the Marketing strategy for Harbourline Life.</li><li>To develop all Marketing materials for the launch, including development response TV commercials and website.</li><li>To develop TV media plan and partner with a New York Media Agency.</li><li>To develop the Acquisition Plan to meet the Year 1 Sales unit targets, within budget.</li><li>To manage the marketing budget to deliver the lead, acquisition, brand, digital, and communications objectives.</li><li>To take ownership of the annual acquisition budget setting process.</li><li>To ensure the customer retention strategy is in place to achieve the financial targets for customer retention.</li><li>To manage the Marketing project plan to deadline, given the critical path predominantly marketing.</li><li>To develop relationships and engage with all external business partners, including Marketing Suppliers, Call Centre Operators, the Insurer and their Consultants, Printers and Mail houses, Telephony providers, Recruiters, and Legal Counsel.</li><li>Participate in decision making and strategic discussion for broad business planning, projects, investment decisions and strategy.</li></ul>
    </div></div>
    <div class="row"><span>Reporting to -</span><span>Reporting to - CEO, Northgate Life Distribution US</span></div>
    <div class="row"><span>Key Relationships -</span><div class="col"><p>Key stakeholder relationships with -</p><p>Five owners of Northgate Life Distribution, Alpen Re US (a reinsurer), and Meridian Mutual (the insurance company).</p><p>Being a start up, whilst strategic, this role was naturally 'sleeves rolled up and hands on'.</p><p>The role in the US was a 12 month contract, before a planned return to Northgate Life Distribution (UK) as the Chief Marketing Officer. Unfortunately, this did not happen, as my husband was diagnosed with a serious illness in August 2015.</p></div></div>
  </div>
  <div class="role" style="top:264px">
    <div class="row"><span class="date">MARCH 2014 TO AUGUST 2014</span><span>Head of Marketing &amp; General Manager - Business Operations<br>Northgate Life Distribution (UK) - Prentis Life, consumer life insurance brand</span></div>
    <div class="row"><span>Role responsibilities -</span><div class="col">
      <p>This role was a 3 month contract.</p>
      <p>The overarching objectives of the 3 month relocation to London were to -</p>
      <ul><li>To prepare NLD UK for the launch of the Direct Life Insurance brand.</li><li>To leave the NLD UK in a prepared position for the CEO &amp; NLD team to successfully launch the brand to the agreed timeline.</li></ul>
      <p>The primary objectives of the General Manager Marketing &amp; Business Operations -</p>
      <ul><li>To obtain financial services license for NLD (Direct Authorisation &amp; Appointed Rep Status).</li><li>To establish the Sales Call Centre from end &amp; lead management processes.</li><li>To develop the Acquisition Plan to meet the Year 1 Sales unit targets, within budget.</li><li>To shortlist Creative Agencies for selection by the CEO, UK.</li><li>To shortlist Marketing roles and Support roles for selection by the CEO, UK.</li><li>To develop the project plan, and to understand and outline the critical path.</li><li>Develop relationships &amp; pursue engagement with all external business partners, including Marketing Suppliers, Call Centre Operators, the Insurer and their Consultants, Printers and Mail houses, Telephony providers, Recruiters, Banks, and Legal Counsel.</li><li>General administration of a start up company overseas.</li></ul>
    </div></div>
    <div class="row"><span>Reporting to -</span><span>Reporting to - Group CEO, Northgate Life Distribution</span></div>
    <div class="row"><span>Key Relationships -</span><div class="col"><p>Key stakeholder relationships with -</p><p>Five owners of Northgate Life Distributions, including Alpen Re UK</p></div></div>
  </div>
  <div class="band bottom"></div>
</section>
<div class="page-label" style="left:426px;top:542px">PAGE - 02</div>

<!-- PAGE 3 -->
<section class="page" style="left:831px;top:36px">
  <div class="band top"></div>
  <div class="role" style="top:30px">
    <div class="row"><span class="date">DECEMBER 2012 TO MAY 2013</span><span>Commercial &amp; MIS Advisor<br>Keel Assurance Ltd</span></div>
    <div class="row"><span>Role responsibilities -</span><div class="col">
      <p>The primary objectives of the Commercial &amp; MIS Advisor / Manager are to -</p>
      <ul><li>Deliver commercial insights and advise the Senior Management Team regularly in all areas of the business including: Acquisition, the existing book (customers), financial performance, and the external environment.</li><li>Direct the development and implementation of Management Information Systems and Systems for Keel Direct.</li><li>Direct the development of commercial modelling for Keel Direct including: Acquisition, Retention, Claims, Policy Administration, corporate overheads.</li><li>Produce reporting for the Executive regularly and as required.</li><li>Communicate the Financial statements to key stakeholders to inform future performance decisions.</li><li>Collaborating with strategic leaders who will contribute to the future growth of Keel Direct to ensure support is well placed to achieve corporate goals.</li></ul>
    </div></div>
    <div class="row" style="margin-top:18px"><span>Reporting to -</span><span>Primary key stakeholders will be considered internal customers. Primary Customer Engagement will be with:</span></div>
    <div class="row"><span>Key Relationships -</span><div class="stack"><span>The Commercial Director</span><span>The Chief Customer Officer</span><span>Chief Marketing Officer</span></div></div>
  </div>
  <div class="role" style="top:223px">
    <div class="row"><span class="date">JULY 2012 TO DECEMBER 2012</span><span>Head of Marketing Operations – Acquisition and Retention<br>Keel Assurance Ltd</span></div>
    <div class="row"><span>Role responsibilities -</span><div class="col">
      <p>Primary responsibilities are to -</p>
      <ul><li>Collaborate with strategic leaders who will contribute to the future growth of Keel Direct.</li><li>Deliver commercial insights and recommendations in Acquisition planning, financial performance and the external environment.</li><li>Direct the development of commercial modelling for Acquisition and Retention.</li><li>Produce and communicate the Financial statements and supporting insights to inform future performance decisions.</li><li>Direct the management and implementation of reporting solutions for Keel Direct Acquisition and Retention.</li><li>Direct the implementation of projects impacting all aspects of Marketing.</li></ul>
    </div></div>
    <div class="row" style="margin-top:6px"><span>Reporting to -</span><span>The Head of Marketing Operations engages with senior leadership, delivering outcomes by influencing and leading others.</span></div>
    <div class="row"><span>Key Relationships -</span><div class="stack"><span>Chief Marketing Officer</span><span>New Ventures Director (formerly Joint Chief Operating Officer)</span><span>Commercial Director (formerly Joint Chief Operating Officer)</span><span>GM Call Centre Operations</span><span>Marketing Leadership Team</span><span>Head of Sales</span></div></div>
  </div>
  <div class="band bottom"></div>
</section>
<div class="page-label" style="left:831px;top:542px">PAGE - 03</div>

<!-- PAGE 4 -->
<section class="page" style="left:213px;top:618px">
  <div class="band top"></div>
  <div class="role" style="top:36px">
    <div class="row"><span class="date">OCTOBER 2010 TO JULY 2012</span><span>P&amp;L / Brand Manager – CoverPoint<br>Part of the Spire Group</span></div>
    <div class="row" style="margin-top:8px"><span>Role responsibilities -</span><div class="col">
      <p>The primary objectives of the P&amp;L / Brand Manager – CoverPoint -</p>
      <ul><li>To deliver revenue to achieve CoverPoint Direct growth objectives.</li><li>To manage costs to achieve CoverPoint Direct profit objectives.</li><li>To actively drive strategic projects within CoverPoint Direct, which contribute to other revenue or profit objectives, or both.</li><li>To contribute to the delivery of the revenue &amp; profit objectives of the Alliance partners.</li><li>To develop strategies for CoverPoint and the broader Direct business, by understanding how CoverPoint fits within Spire Group.</li><li>Budget preparation, management monthly &amp; accountability.</li><li>Reporting of the P&amp;L.</li><li>Engage key internal stakeholders to ensure financial objectives are achieved.</li></ul>
    </div></div>
    <div class="row" style="margin-top:14px"><span>Reporting to -<br>Key Relationships -</span><div class="stack"><span>Key stakeholder relationships with -</span><span>Three P&amp;L / Brand Managers – Alliance Partners</span><span>Two Joint CEO</span><span>Head of Sales</span><span>Head of Product</span><span>Head of Marketing</span></div></div>
  </div>
  <div class="role" style="top:248px">
    <div class="row"><span class="date">JANUARY 2010 TO OCTOBER 2010</span><span>Product Portfolio Marketing Manager – CoverPoint<br>Part of the Spire Group</span></div>
    <div class="row" style="margin-top:8px"><span>Role responsibilities -</span><div class="col">
      <p>The primary objectives of the Product Portfolio Marketing Manager – CoverPoint -</p>
      <ul><li>To deliver product life cycle management of current and future planned CoverPoint products.</li><li>To direct the Marketing Managers and respective suppliers to achieve lead volumes at required cost metrics.</li><li>To actively manage a team of 4 Marketing Managers to achieve their objectives.</li><li>To communicate Marketing plans and objectives to key stakeholders within CoverPoint, from Senior Management to Call Centre Managers.</li><li>To prepare short, medium, and long term budgets. Analyse each quarter, reforecast, and accountability.</li></ul>
    </div></div>
    <div class="row" style="margin-top:6px"><span>Reporting to -</span><span>The Head of Marketing Operations engages with senior leadership, delivering outcomes by influencing and leading others.</span></div>
    <div class="row"><span>Key Relationships -</span><div class="stack"><span>Key stakeholder relationships with -</span><span>General Manager Marketing</span><span>Marketing Communications Manager</span><span>Digital Marketing Manager</span></div></div>
  </div>
  <div class="band bottom"></div>
</section>
<div class="page-label" style="left:213px;top:1134px">PAGE - 04</div>

<!-- PAGE 5 -->
<section class="page" style="left:623px;top:618px">
  <div class="band top"></div>
  <div class="role" style="top:22px">
    <div class="row"><span class="date">JANUARY 2008 TO OCTOBER 2010</span><span>Marketing Manager<br>CoverPoint Pty Ltd</span></div>
    <div class="row" style="margin-top:10px"><span>Role responsibilities -</span><div class="col">
      <p>The primary objectives of the Marketing Manager -</p>
      <ul><li>To develop, monitor and implement acquisition strategy and plans including the introduction of new products cost effectively to market, inbound and outbound acquisition/upgrade/cross-sell activity.</li><li>Delivery of leads, profitability, product mix and channel targets by individual product and across the full product portfolio.</li><li>To develop and manage media strategy and new acquisition channel development to achieve leads and CPA requirements.</li><li>To identify and negotiate agreements with 3rd party channel partners for lead generation.</li><li>Manage all external media partners.</li><li>Report on marketing activity and results to the Senior Management team.</li></ul>
    </div></div>
    <div class="row" style="margin-top:10px"><span>Reporting to -<br>Key Relationships -</span><div class="stack"><span>Key stakeholder relationships with -</span><span>General Manager, Acquisition</span><span>Marketing Communications Manager</span><span>Digital Marketing Manager</span><span>Senior Management Team</span></div></div>
  </div>

  <div class="contact-icon"><svg width="10" height="10" viewBox="0 0 24 24" aria-hidden="true"><path d="M7 4l3 4-2 2c1 2 3 4 5 5l2-2 4 3-2 3c-6 0-12-6-12-12z" fill="#fff"/></svg></div>
  <div class="contact-bar">FOR INFORMATION ON PREVIOUS ROLES, PLEASE CONTACT ME AT MARISOL.T@MAILBOX.EXAMPLE OR 0400 555 218</div>

  <div class="p5-sec" style="top:236px">
    <h2 class="sec-head">QUALIFICATIONS<span class="bar"></span></h2>
    <p class="small-note">Degrees and Awards of relevance -</p>
    <div class="q-grid">
      <div class="tl"><div><span>Institution</span><span>Eastbay Technical University</span></div><div><span>Degree</span><span>Bachelor of Business, Major in Marketing and Small Business</span></div><div><span>Dates</span><span>January 1993 to June 1997</span></div></div>
      <div class="tl"><div><span>Institution</span><span>Keel Assurance Ltd</span></div><div><span>Degree</span><span>Outstanding Achievement Award 2009</span></div><div><span>Dates</span><span>December 2009</span></div></div>
      <div class="tl"><div><span>Institution</span><span>CoverPoint Pty Ltd</span></div><div><span>Degree</span><span>Employee of the Year Award 2005</span></div><div><span>Dates</span><span>December 2005</span></div></div>
      <div class="tl"><div><span>Institution</span><span>Keel Assurance Ltd</span></div><div><span>Degree</span><span>Overall Company Achievement Award 2009</span></div><div><span>Dates</span><span>December 2009</span></div></div>
    </div>
  </div>

  <div class="p5-sec" style="top:396px">
    <h2 class="sec-head">EXECUTIVE EDUCATION<span class="bar"></span></h2>
    <div class="ee-grid">
      <div class="tl"><div><span>Institution</span><span>Keel Assurance Ltd</span></div><div><span>Program</span><span>Keel Senior Leaders Strategy Program</span></div><div><span>Dates</span><span>April 2012 to Current</span></div></div>
      <div class="tl"><div><span>Institution</span><span>Keel Assurance Ltd</span></div><div><span>Program</span><span>Equip Leadership Program</span></div><div><span>Dates</span><span>February 2009 to April 2010</span></div></div>
      <div class="tl"><div><span>Institution</span><span>Southbank Academy, VIC</span></div><div><span>Program</span><span>Certificate IV in Business, Frontline Management</span></div><div><span>Dates</span><span>Completed October 2008</span></div></div>
    </div>
  </div>
  <div class="band bottom"></div>
</section>
<div class="page-label" style="left:623px;top:1134px">PAGE - 05</div>

</body>
</html>
```